Business Cards

We are wanting business cards created using previous design #36167008 as a starting point.
Info needed on front side:
Employee Name
Title
Email
Phone Number

Info needed on back side: (these are our product lines)
Frac Valves Fishing
Flowback Thru-Tubing
Torque & Test LMQV

please see changes

```html
<!DOCTYPE html>
<html lang="en">
<head>
<meta charset="utf-8">
<title>Business Cards</title>
<link rel="stylesheet" href="https://fonts.googleapis.com/css2?family=Montserrat:wght@300;400;700&display=swap">
<style>
  :root {
    --stage: #232323;
    --card: #000000;
    --ink: #ffffff;
    --ink-soft: #e6e6e6;
  }
  * { margin: 0; padding: 0; box-sizing: border-box; }
  html, body {
    width: 1200px;
    height: 780px;
    overflow: hidden;
    background: var(--stage);
    font-family: "Montserrat", Arial, sans-serif;
    color: var(--ink);
  }
  .sheet {
    position: relative;
    width: 1200px;
    height: 780px;
  }
  .card {
    position: absolute;
    top: 236px;
    width: 540px;
    height: 309px;
    background: var(--card);
    border-radius: 28px;
  }
  .card--back { left: 40px; }
  .card--front { left: 620px; }

  .product-lines {
    position: absolute;
    left: 150px;
    top: 104px;
    font-weight: 700;
    font-size: 26px;
    line-height: 34px;
    letter-spacing: 0.3px;
  }
  .product-lines li { list-style: none; white-space: nowrap; }
  .product-lines li:nth-child(3) { padding-left: 30px; }

  .identity {
    position: absolute;
    right: 215px;
    top: 160px;
    text-align: right;
  }
  .identity__name {
    font-weight: 700;
    font-size: 30px;
    line-height: 34px;
    white-space: nowrap;
  }
  .identity__title {
    font-weight: 300;
    font-size: 14px;
    line-height: 20px;
    color: var(--ink-soft);
    margin-top: 2px;
  }
  .divider {
    position: absolute;
    left: 345px;
    top: 112px;
    width: 1.5px;
    height: 110px;
    background: var(--ink);
  }
  .contact {
    position: absolute;
    left: 368px;
    top: 128px;
    font-weight: 300;
    font-size: 14px;
    line-height: 24px;
    color: var(--ink-soft);
  }
  .contact li {
    list-style: none;
    display: flex;
    align-items: center;
    gap: 7px;
    white-space: nowrap;
  }
  .contact svg { width: 13px; height: 13px; flex: none; }
</style>
</head>
<body>
<main class="sheet">
  <section class="card card--back" aria-label="Card back: product lines">
    <ul class="product-lines">
      <li>Frac Valves Fishing</li>
      <li>Flowback Thru-Tubing</li>
      <li>Torque &amp; Test LMQV</li>
    </ul>
  </section>

  <section class="card card--front" aria-label="Card front: contact details">
    <div class="identity">
      <p class="identity__name">Employee Name</p>
      <p class="identity__title">Managing Director</p>
    </div>
    <span class="divider" aria-hidden="true"></span>
    <ul class="contact">
      <li>
        <svg viewBox="0 0 16 16" aria-hidden="true"><path fill="#fff" d="M2 6c0-2 3-3.5 6-3.5S14 4 14 6v1.2h-3V5.8H5v1.4H2zM4 8h8l2 5.5H2zM8 9.3a1.6 1.6 0 1 0 0 3.2 1.6 1.6 0 0 0 0-3.2z"/></svg>
        <span>123 456 789</span>
      </li>
      <li>
        <svg viewBox="0 0 16 16" aria-hidden="true"><path fill="#fff" d="M1 3h14v10H1zm1.6 1.2L8 8.4l5.4-4.2zM2.2 5.3v6.5h11.6V5.3L8 9.8z"/></svg>
        <span>info@yourmail.com</span>
      </li>
    </ul>
  </section>
</main>
</body>
</html>
```